Consulting, Investors, Joint Venture Website

Founded in April 2018, Marendo Advisers Limited (MAL) is an advisory consulting firm specializing in engaging investors in business ventures in Tanzania.
With extensive experience in construction, energy, oil and gas and the legal professions, our team assembles our expertise that allows foreign investors to set foot and flourish in the Tanzanian market.
MAL is locally owned, founded and registered. Our shareholders are cultured Tanzanian citizens with extensive corporate experience in South Africa, Tanzania, United Kingdom and the United States.

Our mission is to provide responsive and unrivalled professional advice from learned and experienced professionals versed in the local market, with an understanding of the cultural and logistical challenges faced by foreign investors.

Our vision is to provide a complete investor’s package that initiates with company registration, compliance and documentation services and ultimately operational facilitation services.

Target Market(s)

Foreign Investors, International companies

Industry/Entity Type

Business Consultant

Number of Pages Required

5+ page

Requirements
Must have
• It will be 5 pages - Home, About Us, Services, Portfolio, Contact Us
Nice to have
• if it can look like https://www.vq-sample.com/
• or https://www.torvell.com or http://www.bramwickpoint.com/

```html
<!DOCTYPE html>
<html lang="en">
<head>
<meta charset="utf-8">
<title>Marendo Advisers – Consulting for Foreign Investors</title>
<link rel="stylesheet" href="https://fonts.googleapis.com/css2?family=Lato:wght@400;700&family=Raleway:wght@400;500;600;700&display=swap">
<style>
  :root{
    --blue:#1f5db3;
    --blue-light:#2a6fd0;
    --ink:#111111;
    --dark:#161616;
    --heading:#1c1c1c;
    --muted:#8d8d8d;
    --cell:#e8e8e8;
    --page:#f6f6f6;
    --white:#ffffff;
  }
  *{box-sizing:border-box;margin:0;padding:0}
  html,body{width:1200px;height:2752px;overflow:hidden;background:var(--white)}
  body{position:relative;font-family:"Raleway",Arial,sans-serif;color:var(--heading)}
  .abs{position:absolute}

  /* header */
  .site-header{left:11px;top:11px;width:1178px;height:92px;background:var(--ink)}
  .brand{left:105px;top:20px;display:flex;align-items:center;gap:14px;color:#3f86e0;
    font-family:"Raleway",sans-serif;font-weight:700;font-size:32px;letter-spacing:2px}
  .brand-square{width:44px;height:44px;background:#3f86e0}
  .top-pill{top:0;height:37px;background:var(--blue);color:var(--white);font-size:14px;
    display:flex;align-items:center;justify-content:center;gap:8px;border-radius:0 0 3px 3px}
  .follow-pill{left:738px;width:205px}
  .call-pill{left:956px;width:116px}
  .dot-icon{width:10px;height:10px;border-radius:50%;background:var(--white)}
  .main-nav a{position:absolute;top:52px;color:#cfcfcf;font-size:17px;text-decoration:none}
  .main-nav a.is-active{color:#3f86e0}

  /* hero */
  .hero{left:11px;top:103px;width:1178px;height:570px;
    background:linear-gradient(120deg,#46566a 0%,#8a9bb0 35%,#b7c3cf 60%,#6f7f92 100%)}
  .hero-title{left:108px;top:180px;font-family:"Raleway",sans-serif;font-weight:700;font-size:44px;color:var(--white)}
  .hero-sub{left:108px;top:240px;font-size:25px;line-height:28px;color:var(--white)}
  .btn{position:absolute;background:var(--blue);color:var(--white);font-weight:600;border-radius:4px;
    display:flex;align-items:center;justify-content:center}
  .hero-btn{left:108px;top:314px;width:164px;height:40px;font-size:23px}
  .scroll-cue{left:573px;top:505px}

  /* welcome */
  .welcome{left:11px;top:673px;width:1178px;height:323px;background:var(--page)}
  .section-title{position:absolute;left:0;width:100%;text-align:center;font-family:"Lato",sans-serif;font-size:33px;color:var(--heading)}
  .section-copy{position:absolute;left:200px;width:778px;text-align:center;font-size:15px;line-height:20px;color:var(--muted)}
  .section-btn{width:163px;height:38px;font-size:21px;left:507px}

  /* services grid */
  .services{left:11px;top:996px;width:1178px;height:643px;display:grid;grid-template-columns:repeat(4,1fr);grid-template-rows:repeat(2,1fr)}
  .service-photo{width:100%;height:100%}
  .service-card{background:var(--cell);padding:36px 30px 0 38px}
  .service-card h3{font-family:"Lato",sans-serif;font-weight:700;font-size:27px;line-height:31px;color:var(--heading);text-transform:uppercase}
  .service-card .tagline{color:var(--blue);font-size:20px;margin:12px 0 24px}
  .service-card p{color:var(--muted);font-size:15px;line-height:20px}

  /* case study */
  .case-study{left:11px;top:1639px;width:1178px;height:869px;background:linear-gradient(180deg,#f7f7f7 0%,#e9e9e9 55%,#d6d6d6 100%)}
  .case-sub{position:absolute;left:0;width:100%;text-align:center;color:var(--blue);font-size:21px}
  .diamond-label{fill:var(--white);text-anchor:middle;font-family:"Lato",sans-serif}

  /* footer */
  .footer-band{left:11px;top:2508px;width:1178px;height:162px;background:linear-gradient(100deg,#0f0f0f 0%,#2a2a2a 50%,#151515 100%)}
  .footer-title{left:116px;top:2550px;font-size:29px;font-weight:600;color:var(--white)}
  .footer-btn{left:807px;top:2551px;width:279px;height:42px;font-size:23px;font-weight:500}
  .footer-nav a,.footer-nav span{position:absolute;top:2629px;color:var(--white);font-size:18px;text-decoration:none;font-weight:500}
  .footer-bar{left:11px;top:2670px;width:1178px;height:73px;background:var(--ink)}
  .copyright{left:116px;top:2697px;color:#bdbdbd;font-size:17px}
  .footer-follow{left:824px;top:2697px;color:#bdbdbd;font-size:17px;display:flex;align-items:center;gap:18px}
  .footer-follow i{width:18px;height:18px;border-radius:50%;background:var(--white);display:block}
</style>
</head>
<body>

<header class="abs site-header">
  <div class="abs brand"><span class="brand-square"></span>MARENDO ADVISERS</div>
  <div class="abs top-pill follow-pill">Follow us on <i class="dot-icon"></i><i class="dot-icon"></i><i class="dot-icon"></i></div>
  <div class="abs top-pill call-pill">Call us now</div>
  <nav class="main-nav">
    <a class="is-active" style="left:649px">Home</a>
    <a style="left:767px">About</a>
    <a style="left:875px">Services</a>
    <a style="left:1004px">Contact</a>
  </nav>
</header>

<section class="abs hero" role="img" aria-label="Photo of a consultant's hand resting on business papers at a desk">
  <h1 class="abs hero-title" style="left:97px;top:180px">MARENDO ADVISERS</h1>
  <p class="abs hero-sub" style="left:97px;top:240px">Foreign Investors, International Companies<br>International Companies.</p>
  <a class="btn hero-btn" style="left:108px;top:314px">Get Started</a>
  <svg class="abs scroll-cue" width="56" height="40" viewBox="0 0 56 40" aria-hidden="true">
    <polyline points="4,6 28,20 52,6" fill="none" stroke="#fff" stroke-width="5"/>
    <polyline points="4,20 28,34 52,20" fill="none" stroke="#fff" stroke-width="5"/>
  </svg>
</section>

<section class="abs welcome">
  <h2 class="section-title" style="top:50px">Welcome to Marendo Advisers</h2>
  <p class="section-copy" style="top:105px">Lorem Ipsum is simply dummy text of the printing and type setting industry. Lorem Ipsum is simply dummy text of the printing and type setting industry. Lorem Ipsum is simply dummy text of the printing and type setting industry. Lorem Ipsum is simply dummy text of the printing and type setting industry. Lorem Ipsum is simply dummy text of the printing and type setting industry. Lorem Ipsum is simply dummy text of the printing and type setting industry.</p>
  <a class="btn section-btn" style="top:241px">Read More</a>
</section>

<section class="abs services">
  <div class="service-photo" role="img" aria-label="Construction crane against a blue sky" style="background:linear-gradient(160deg,#2f7fc6,#8cbbe0 60%,#b79a6a)"></div>
  <article class="service-card"><h3>Strategy<br>Consulting</h3><p class="tagline">Mapping your Journey</p><p>Lorem Ipsum is simply dummy text of the printing and type setting industry. Lorem Ipsum is simply dummy text of the printing and type setting industry.</p></article>
  <div class="service-photo" role="img" aria-label="Business people playing chess on a table with documents" style="background:linear-gradient(150deg,#f2f2f2,#d9c7a7 50%,#6b4a2a)"></div>
  <article class="service-card"><h3>Change<br>Management</h3><p class="tagline">Build Sustainability</p><p>Lorem Ipsum is simply dummy text of the printing and type setting industry. Lorem Ipsum is simply dummy text of the printing and type setting industry.</p></article>
  <article class="service-card"><h3>Strategy<br>Consulting</h3><p class="tagline">Mapping your Journey</p><p>Lorem Ipsum is simply dummy text of the printing and type setting industry. Lorem Ipsum is simply dummy text of the printing and type setting industry.</p></article>
  <div class="service-photo" role="img" aria-label="Power plant cooling towers above autumn trees" style="background:linear-gradient(180deg,#c9d3dc,#8e8e86 55%,#d7a826)"></div>
  <article class="service-card"><h3>Strategy<br>Consulting</h3><p class="tagline">Mapping your Journey</p><p>Lorem Ipsum is simply dummy text of the printing and type setting industry. Lorem Ipsum is simply dummy text of the printing and type setting industry.</p></article>
  <div class="service-photo" role="img" aria-label="Hand writing growth figures in a notebook" style="background:linear-gradient(140deg,#8a3a1c,#e9e9e9 45%,#f4f4f4)"></div>
</section>

<section class="abs case-study">
  <h2 class="section-title" style="top:62px">Case Study</h2>
  <p class="case-sub" style="top:110px">Building a Digital vision for customer Experience</p>
  <p class="section-copy" style="top:158px">Lorem Ipsum is simply dummy text of the printing and type setting industry. Lorem Ipsum is simply dummy text of the printing and type setting industry.</p>
  <a class="btn section-btn" style="top:218px">Read More</a>
  <svg class="abs" style="left:0;top:0" width="1178" height="869" viewBox="0 0 1178 869">
    <defs>
      <linearGradient id="refinery" x1="0" y1="0" x2="0" y2="1"><stop offset="0" stop-color="#1d3a66"/><stop offset="1" stop-color="#3b4250"/></linearGradient>
      <linearGradient id="pylon" x1="0" y1="0" x2="0" y2="1"><stop offset="0" stop-color="#3d5f8c"/><stop offset="0.6" stop-color="#e3a23a"/><stop offset="1" stop-color="#2a1d10"/></linearGradient>
      <linearGradient id="scaffold" x1="0" y1="0" x2="0" y2="1"><stop offset="0" stop-color="#f2b43a"/><stop offset="1" stop-color="#6b3f10"/></linearGradient>
      <linearGradient id="solar" x1="0" y1="0" x2="1" y2="1"><stop offset="0" stop-color="#b7cde4"/><stop offset="0.45" stop-color="#1f3d7a"/><stop offset="1" stop-color="#0e1c3f"/></linearGradient>
    </defs>
    <polygon role="img" aria-label="Refinery lit at dusk" points="334,290 569,525 334,760 99,525" fill="url(#refinery)"/>
    <polygon role="img" aria-label="Silhouette of an electricity pylon at sunset" points="661,298 801,438 661,578 521,438" fill="url(#pylon)"/>
    <polygon role="img" aria-label="Workers on scaffolding at sunset" points="587,548 727,688 587,828 447,688" fill="url(#scaffold)"/>
    <polygon role="img" aria-label="Rows of solar panels" points="901,383 1118,600 901,817 684,600" fill="url(#solar)"/>
    <text class="diamond-label" x="334" y="518" font-size="27">Lorem Ipsum</text>
    <text class="diamond-label" x="334" y="546" font-size="19" font-family="Raleway,sans-serif">Market Resurch #2</text>
  </svg>
</section>

<footer>
  <div class="abs footer-band" role="img" aria-label="Dimmed photo of hands on a laptop keyboard"></div>
  <h2 class="abs footer-title">Feel Free To Communicate</h2>
  <a class="btn footer-btn">Book an Appointment!</a>
  <nav class="footer-nav">
    <a style="left:116px">Home</a><span style="left:213px">&bull;</span>
    <a style="left:257px">About</a><span style="left:358px">&bull;</span>
    <a style="left:398px">Services</a><span style="left:506px">&bull;</span>
    <a style="left:538px">Case Studies</a><span style="left:684px">&bull;</span>
    <a style="left:716px">Our Team</a><span style="left:833px">&bull;</span>
    <a style="left:872px">Process</a><span style="left:980px">&bull;</span>
    <a style="left:1015px">Contact</a>
  </nav>
  <div class="abs footer-bar"></div>
  <p class="abs copyright">2020 copyright by the business group</p>
  <div class="abs footer-follow">Follow us on <i></i><i></i><i></i></div>
</footer>

</body>
</html>
```